Need simple and modern looking business card with all my information on one side and logo on the other side
Info :
Company name - VELMAR CONSTRUCTION LLC
Company addres- 418 harbor 87th. Dunmoor park ny 10352
Email- velmarllc@tridomail.Com
Company phone number 555-318-6094
Cell number- 555-742-0583
Web site - velmarllc.Com
My name Gerald tomasino

Target Market(s)

Construction , home improvement, remodeling

Industry/Entity Type

Construction

Contact Information for Business Card

It has to be moder but at the same time simple

Font styles to use
Sans Serif

Colors
0255a3
ffffff
000000
f78f20
b1b1b1
9d9d9d
1b1b1b
33a6d7
ec1f27

Requirements
Must have
• My logo on one side maybe with a some kind of background on the other side all my information
Nice to have
• Some kind of background pictures provided by you .PLEASE HAVE ACCOUNT WITH PIXELVAULT WILL NOT PAY ANY EXTRA FEES .
Should not have
• Any kind of hamer, nails,screws, helmets itp. Please do not copy the other designs come up with something new.

```html
<!DOCTYPE html>
<html lang="en">
<head>
<meta charset="utf-8">
<title>Velmar Construction LLC — Business Card</title>
<link rel="stylesheet" href="https://fonts.googleapis.com/css2?family=Exo+2:wght@300;400;500;600&family=Open+Sans:wght@400;600&display=swap">
<style>
  :root {
    --backdrop: #2a2729;
    --card-black: #0b0b0b;
    --card-dark: #1b1b1b;
    --silver: #d9d9d9;
    --silver-mid: #b1b1b1;
    --silver-dim: #9d9d9d;
    --white: #ffffff;
    --accent-orange: #f78f20;
    --accent-blue: #33a6d7;
    --accent-red: #ec1f27;
    --deep-blue: #0255a3;
  }
  * { box-sizing: border-box; margin: 0; padding: 0; }
  html, body {
    width: 1200px;
    height: 1200px;
    overflow: hidden;
    background: var(--backdrop);
  }
  .canvas {
    width: 1200px;
    height: 1200px;
    display: flex;
    flex-direction: column;
    align-items: center;
    justify-content: center;
    gap: 70px;
  }
  .card {
    position: relative;
    width: 880px;
    height: 503px;
    border-radius: 22px;
    overflow: hidden;
    background:
      repeating-linear-gradient(0deg, rgba(255,255,255,0.025) 0 1px, transparent 1px 3px),
      radial-gradient(ellipse at 50% 45%, #3a3a3a 0%, var(--card-dark) 45%, var(--card-black) 80%);
    box-shadow: 0 14px 40px rgba(0,0,0,0.55);
  }

  /* Info side */
  .card--info { padding: 70px 80px; color: var(--silver); }
  .holder-name {
    font-family: "Exo 2", sans-serif;
    font-weight: 500;
    font-size: 62px;
    letter-spacing: 3px;
    text-transform: uppercase;
    color: var(--silver);
    text-align: center;
    margin-top: 20px;
  }
  .details {
    display: flex;
    justify-content: center;
    gap: 70px;
    margin-top: 26px;
  }
  .details__company {
    text-align: right;
    font-family: "Open Sans", sans-serif;
    font-size: 20px;
    line-height: 1.45;
    color: var(--silver-mid);
  }
  .details__company .company-name {
    font-weight: 600;
    font-size: 18px;
    letter-spacing: 0.5px;
    color: var(--silver);
  }
  .details__contact {
    list-style: none;
    font-family: "Open Sans", sans-serif;
    font-size: 20px;
    line-height: 1.45;
    color: var(--silver);
  }
  .details__contact li { display: flex; align-items: center; gap: 12px; }
  .details__contact svg { width: 16px; height: 16px; fill: none; stroke: var(--silver); stroke-width: 1.8; }
  .website-row {
    display: flex;
    align-items: center;
    gap: 26px;
    margin-top: 40px;
  }
  .website-row .rule { flex: 1; height: 1px; background: var(--silver-dim); }
  .website {
    font-family: "Exo 2", sans-serif;
    font-weight: 400;
    font-size: 26px;
    letter-spacing: 12px;
    text-transform: uppercase;
    color: var(--silver);
  }

  /* Brand side */
  .card--brand { display: flex; align-items: center; justify-content: center; gap: 26px; }
  .brand-mark {
    width: 34px;
    height: 34px;
    background: var(--accent-orange);
  }
  .brand-name {
    font-family: "Exo 2", sans-serif;
    font-weight: 400;
    font-size: 50px;
    letter-spacing: 6px;
    color: var(--silver);
    text-transform: uppercase;
  }
</style>
</head>
<body>
  <main class="canvas">
    <section class="card card--info" aria-label="Card front with contact details">
      <h1 class="holder-name">Gerald Tomasino</h1>
      <div class="details">
        <div class="details__company">
          <p class="company-name">VELMAR CONSTRUCTION LLC</p>
          <p>418 harbor 87th.</p>
          <p>Dunmoor park ny 10352</p>
        </div>
        <ul class="details__contact">
          <li>
            <svg viewBox="0 0 16 16" aria-hidden="true"><path d="M4 2h3l1 3-2 1.5a8 8 0 0 0 3.5 3.5L11 8l3 1v3a2 2 0 0 1-2 2A10 10 0 0 1 2 4a2 2 0 0 1 2-2z"/></svg>
            555-318-6094
          </li>
          <li>
            <svg viewBox="0 0 16 16" aria-hidden="true"><rect x="4" y="1.5" width="8" height="13" rx="1.5"/><line x1="7" y1="12" x2="9" y2="12"/></svg>
            555-742-0583
          </li>
          <li>
            <svg viewBox="0 0 16 16" aria-hidden="true"><rect x="1.5" y="3.5" width="13" height="9" rx="1"/><path d="M1.5 4l6.5 5 6.5-5"/></svg>
            velmarllc@tridomail.com
          </li>
        </ul>
      </div>
      <div class="website-row">
        <span class="rule"></span>
        <span class="website">velmarllc.com</span>
        <span class="rule"></span>
      </div>
    </section>

    <section class="card card--brand" aria-label="Card back with company name">
      <span class="brand-mark" aria-hidden="true"></span>
      <span class="brand-name">Velmar Construction LLC</span>
    </section>
  </main>
</body>
</html>
```